Pelican Ridge Toppers, INC Roof Safety Info Marketing Material

We need a flyer to illustrate roof safety methods we offer with the pictures and descriptions uploaded. We are a Dallas-based commercial roofing company named Pelican Ridge Toppers, INC.
We would like to incorporate our dark blues (seen on our website logo). The final design should communicate roof safety and our ability to assess any roof system based on their safety needs.
https://pelicanridgetop.example/company/about-pelican-ridge-toppers-inc/

Target Market(s)

Construction industry

Industry/Entity Type

Commercial Roofind

Font styles to use
Serif

```html
<!DOCTYPE html>
<html lang="en">
<head>
<meta charset="utf-8">
<title>Pelican Ridge Toppers, INC – Roof Safety Flyer</title>
<link href="https://fonts.googleapis.com/css2?family=Bebas+Neue&family=Poppins:wght@400;500;600;700&display=swap" rel="stylesheet">
<style>
:root{
  --navy:#0b2a55;
  --ink:#0a1c38;
  --blue:#0d3e83;
  --accent:#1b4fa0;
  --panel:#dcdde1;
  --text:#1c2430;
  --white:#ffffff;
  --backdrop:#e9eaec;
}
*{margin:0;padding:0;box-sizing:border-box}
html,body{width:1200px;height:2570px;overflow:hidden;background:var(--backdrop)}
body{font-family:'Poppins',sans-serif;color:var(--text);position:relative}
.flyer{position:absolute;left:48px;top:280px;width:1104px;height:1562px;background:var(--white);overflow:hidden;box-shadow:0 10px 30px rgba(0,0,0,.18)}
.flyer-inner{position:absolute;left:0;top:0;width:1004px;height:1420px;transform:scale(1.0996);transform-origin:0 0}
.hero-art{position:absolute;left:0;top:0;width:1004px;height:540px}
.brand{position:absolute;left:70px;top:50px;display:flex;align-items:center;gap:14px}
.brand-dot{width:34px;height:34px;border-radius:50%;background:var(--blue)}
.brand-name{font-family:'Poppins',sans-serif;font-weight:600;font-size:19px;color:var(--navy);letter-spacing:.3px}
.headline{position:absolute;left:40px;top:232px;color:var(--white);font-family:'Bebas Neue',sans-serif;line-height:.88;font-weight:400}
.headline .top{font-size:70px;display:block}
.headline .main{font-size:104px;display:block}
.tagline{position:absolute;left:41px;top:400px;color:var(--white);font-weight:600;font-size:24px}
.safety-line{position:absolute;left:41px;top:472px;color:var(--accent);font-weight:700;font-size:19.5px}

.about{position:absolute;left:595px;top:508px;width:390px;height:812px;background:var(--panel);padding:24px 30px 0 33px;text-align:center}
.about h2{font-size:31px;font-weight:600;color:var(--ink);line-height:1;margin-bottom:12px}
.about p{font-size:14.2px;line-height:18px;color:var(--text)}
.about .justify{text-align:justify;text-align-last:center}
.about h3{font-size:19px;font-weight:600;color:var(--ink);margin:16px 0 14px}
.anchor-item{display:flex;flex-direction:column;align-items:center;margin-bottom:18px}
.anchor-item .pin{width:34px;height:34px;margin-bottom:10px}

.section-tab{position:absolute;left:0;width:270px;height:58px}
.section-tab span{position:absolute;left:42px;top:6px;font-size:31px;font-weight:600;color:var(--white)}
.lead{position:absolute;left:41px;font-size:20px;line-height:24px;color:var(--ink);white-space:nowrap}
.item{position:absolute;left:41px;display:flex;gap:20px;align-items:flex-start;width:548px}
.item svg{flex:0 0 58px}
.item p{font-size:14.4px;line-height:17.6px;color:var(--text);padding-top:2px;letter-spacing:-.1px}
.goal{position:absolute;left:41px;top:1235px;font-size:19.5px;line-height:24px;font-weight:600;color:var(--ink);white-space:nowrap}

.footer{position:absolute;left:0;top:1320px;width:1004px;height:100px}
.cta{position:absolute;left:40px;top:1356px;color:var(--white);font-weight:600;font-size:23px}
.contact{position:absolute;display:flex;align-items:center;gap:8px;color:var(--white);font-size:18px;line-height:22px;white-space:nowrap}
</style>
</head>
<body>
<main class="flyer">
 <div class="flyer-inner">

  <svg class="hero-art" viewBox="0 0 1004 540">
   <defs>
    <linearGradient id="photoTone" x1="0" y1="0" x2="0" y2="1">
     <stop offset="0" stop-color="#8fb8e6"/>
     <stop offset=".35" stop-color="#9aa3ad"/>
     <stop offset="1" stop-color="#4f5660"/>
    </linearGradient>
    <linearGradient id="panelTone" x1="0" y1="0" x2="1" y2="0">
     <stop offset="0" stop-color="#0a1f3d"/>
     <stop offset="1" stop-color="#0d3e83"/>
    </linearGradient>
   </defs>
   <polygon role="img" aria-label="Photo of a roofer in a hard hat and safety vest laying shingles on a sloped roof under blue sky" points="440,0 1004,0 1004,540 565,540 380,160" fill="url(#photoTone)"/>
   <polygon points="0,160 385,160 527,462 0,462" fill="url(#panelTone)"/>
   <polygon points="0,462 527,462 548,510 0,510" fill="#ffffff"/>
   <polygon points="0,510 548,510 565,535 0,535" fill="#0b2a55"/>
  </svg>

  <div class="brand">
   <span class="brand-dot"></span>
   <span class="brand-name">PELICAN RIDGE TOPPERS INC</span>
  </div>

  <h1 class="headline"><span class="top">STATE OF THE</span><span class="main">ART ROOFING</span></h1>
  <div class="tagline">UNIQUE DESIGN &amp; INSTALLATION</div>
  <div class="safety-line">SAFETY FOR YOUR COMMERCIAL ROOFING NEEDS</div>

  <svg class="section-tab" style="top:550px" viewBox="0 0 270 58"><polygon points="0,0 228,0 248,58 0,58" fill="#0b2a55"/><polygon points="232,0 240,0 268,58 260,58" fill="#0a1c38"/></svg>
  <div class="section-tab" style="top:550px"><span>Problems</span></div>
  <div class="lead" style="top:618px">Falls are the leading cause of death in the<br>construction industry.</div>

  <div class="item" style="top:680px">
   <svg viewBox="0 0 58 58" width="58" height="58"><circle cx="29" cy="29" r="27" fill="#fff" stroke="#0d3e83" stroke-width="3"/><circle cx="29" cy="29" r="21" fill="#0d3e83"/><polygon points="29,17 41,38 17,38" fill="none" stroke="#fff" stroke-width="2.2"/><line x1="29" y1="24" x2="29" y2="32" stroke="#fff" stroke-width="2.2"/><circle cx="29" cy="35" r="1.3" fill="#fff"/></svg>
   <p>Roofers encounter many hazards on the job, including dangers associated with working at great heights with power tools, electricity, noise, and extreme temperatures.</p>
  </div>
  <div class="item" style="top:752px">
   <svg viewBox="0 0 58 58" width="58" height="58"><circle cx="29" cy="29" r="27" fill="#fff" stroke="#0d3e83" stroke-width="3"/><circle cx="29" cy="29" r="21" fill="#0d3e83"/><circle cx="29" cy="29" r="10" fill="none" stroke="#fff" stroke-width="2"/><circle cx="29" cy="29" r="3" fill="#fff"/></svg>
   <p>A lack of fall protection, damaged fall protection equipment, or improper setup can drastically increase a roofer's risk of falling.</p>
  </div>
  <div class="item" style="top:822px">
   <svg viewBox="0 0 58 58" width="58" height="58"><circle cx="29" cy="29" r="27" fill="#fff" stroke="#0d3e83" stroke-width="3"/><circle cx="29" cy="29" r="21" fill="#0d3e83"/><rect x="20" y="26" width="10" height="14" fill="none" stroke="#fff" stroke-width="2"/><circle cx="25" cy="21" r="3" fill="none" stroke="#fff" stroke-width="2"/><path d="M33 20 l6 2 v5 c0 4-3 6-6 7 c-3-1-6-3-6-7" fill="none" stroke="#fff" stroke-width="1.8"/></svg>
   <p>Unless these hazards are mitigated by the property owner or employer, contractors and facility representatives alike are at risk for serious injury or death.</p>
  </div>

  <svg class="section-tab" style="top:900px" viewBox="0 0 270 58"><polygon points="0,0 228,0 248,58 0,58" fill="#0b2a55"/><polygon points="232,0 240,0 268,58 260,58" fill="#0a1c38"/></svg>
  <div class="section-tab" style="top:900px"><span>Solution</span></div>
  <div class="lead" style="top:968px">At Pelican Ridge Toppers, safety is our main priority.</div>

  <div class="item" style="top:1005px">
   <svg viewBox="0 0 58 58" width="58" height="58"><circle cx="29" cy="29" r="27" fill="#fff" stroke="#0d3e83" stroke-width="3"/><circle cx="29" cy="29" r="21" fill="#0d3e83"/><rect x="19" y="20" width="9" height="20" fill="none" stroke="#fff" stroke-width="2"/><rect x="30" y="26" width="10" height="14" fill="none" stroke="#fff" stroke-width="2"/></svg>
   <p>Throughout our inspection, our roofing experts assess your building, identifying three main areas of safety protocol. These areas include evidence of rooftop anchorage to provide safe access to your roof, fall protection systems to allow employees and workers to safely operate on your roof, and protection around fall hazards on your rooftop such as skylights, mechanical or ladder areas.</p>
  </div>
  <div class="item" style="top:1145px">
   <svg viewBox="0 0 58 58" width="58" height="58"><circle cx="29" cy="29" r="27" fill="#fff" stroke="#0d3e83" stroke-width="3"/><circle cx="29" cy="29" r="21" fill="#0d3e83"/><circle cx="29" cy="24" r="6" fill="none" stroke="#fff" stroke-width="2"/><path d="M17 36 h10 l6 3 h8" fill="none" stroke="#fff" stroke-width="2"/></svg>
   <p>Following our inspection, our team will thoroughly review and recommend a fall prevention plan that is tailored to your specific needs.</p>
  </div>

  <div class="goal">Our goal is to provide you with a system that is safe,<br>OSHA compliant, and easy to use.</div>

  <section class="about">
   <h2>About Us</h2>
   <p class="justify">Pelican Ridge Toppers INC has been providing quality roofing service options for commercial clients for over twenty years. The company was founded by Dale Whitcomb with a goal of providing excellent and reliable service. After Dale's unfortunate passing in 2003, his wife Marlene took over the business and continues to build upon the strong reputation of Pelican Ridge Toppers INC. Under Marlene's leadership, PRT has grown significantly, achieved many prestigious awards and recognitions, and has become one the premier Commercial Roofing companies in the United States.</p>
   <h3>Pertinent info for roof anchors</h3>
   <div class="anchor-item">
    <svg class="pin" viewBox="0 0 34 34"><circle cx="17" cy="17" r="16" fill="#0d3e83"/><circle cx="17" cy="13" r="4" fill="none" stroke="#fff" stroke-width="1.8"/><path d="M10 25 q7-7 14 0" fill="none" stroke="#fff" stroke-width="1.8"/></svg>
    <p class="justify">The most important thing (fairly new), if there is an accident on a building, the building owner is responsible for that accident. Previously it fell on the property manager.</p>
   </div>
   <div class="anchor-item">
    <svg class="pin" viewBox="0 0 34 34"><circle cx="17" cy="17" r="16" fill="#0d3e83"/><circle cx="17" cy="13" r="4" fill="none" stroke="#fff" stroke-width="1.8"/><path d="M10 25 q7-7 14 0" fill="none" stroke="#fff" stroke-width="1.8"/></svg>
    <p class="justify">OSHA guidelines outlined it. Anything with mechanical equipment or any work within 15 feet of a building edge over 6 feet off the ground. Either guard rails or roof anchors. Its all dependent on your specific situation which is where we come into play. We can make that assessment.</p>
   </div>
   <div class="anchor-item">
    <svg class="pin" viewBox="0 0 34 34"><circle cx="17" cy="17" r="16" fill="#0d3e83"/><circle cx="17" cy="13" r="4" fill="none" stroke="#fff" stroke-width="1.8"/><path d="M10 25 q7-7 14 0" fill="none" stroke="#fff" stroke-width="1.8"/></svg>
    <p class="justify">kylights are a fall-hazard to consider. Roof hatches as well.</p>
   </div>
  </section>

  <svg class="footer" viewBox="0 0 1004 100">
   <rect width="1004" height="100" fill="#0d3e83"/>
   <polygon points="0,0 245,0 288,50 245,100 0,100" fill="#0a1c38"/>
   <polyline points="252,0 292,50 252,100" fill="none" stroke="#ffffff" stroke-width="5"/>
  </svg>
  <div class="cta">CALL US TODAY</div>
  <div class="contact" style="left:312px;top:1357px">
   <svg width="24" height="24" viewBox="0 0 24 24"><path d="M5 2 l4 0 l2 5 l-3 2 c1 3 3 5 6 6 l2-3 l5 2 l0 4 c0 2-1 3-3 3 C9 21 3 15 3 4 c0-1 1-2 2-2z" fill="#fff"/></svg>
   <span>(555) 014-2290</span>
  </div>
  <div class="contact" style="left:492px;top:1357px;font-size:15.5px">
   <svg width="22" height="22" viewBox="0 0 24 24"><circle cx="12" cy="12" r="10" fill="none" stroke="#fff" stroke-width="2"/><ellipse cx="12" cy="12" rx="4.5" ry="10" fill="none" stroke="#fff" stroke-width="1.6"/><line x1="2" y1="12" x2="22" y2="12" stroke="#fff" stroke-width="1.6"/></svg>
   <span>www.pelicanridgetop.example</span>
  </div>
  <div class="contact" style="left:800px;top:1344px;align-items:flex-start;font-size:17px">
   <svg width="18" height="24" viewBox="0 0 18 24"><path d="M9 0 C4 0 0 4 0 9 c0 6 9 15 9 15 s9-9 9-15 C18 4 14 0 9 0z" fill="#fff"/><circle cx="9" cy="9" r="3.5" fill="#0d3e83"/></svg>
   <span>410 Ferncliff Ave<br>Plano, TX 75099</span>
  </div>

 </div>
</main>
</body>
</html>
```